Wine Label for a White and a Red Wine from Italy

We have a very good idea of what we want with artwork. We need you to please design a 'template' with the text so we can change out the artwork from year to year. Samples are shown of what we are looking for. We are looking for options with the two basic designs. Brand name of wine is: Valora di Castegno. Both wines are in a light green Bordeaux-style bottle (note: we don't show a light green bottle in the mockup but please remember the bottle is light green). Artwork is provided. We'd like to see either the green or blue butterfly on the white wine, the red butterfly is for the red wine. Please base the design on the attached label from Brailey and/or the attached label from Chateau Mervanges.

Target Market(s)

Millennials, women

Requirements
Must have
• The artwork (butterflies) attached.
Nice to have
• Elegant, readable fonts. Please make the text so it can be changed by the printer. Please make it so the artwork can be changed too.

```html
<!DOCTYPE html>
<html lang="en">
<head>
<meta charset="utf-8">
<title>Valora di Castegno – Barrel Select Labels</title>
<link rel="stylesheet" href="https://fonts.googleapis.com/css2?family=Pinyon+Script&family=Josefin+Sans:wght@300;400&family=Cinzel:wght@600&display=swap">
<style>
  :root {
    --page: #ffffff;
    --label-paper: #f1efea;
    --ink: #141210;
    --accent-red: #b0271f;
    --gold: #ad9664;
    --seal-line: #b59f72;
    --art-orange: rgba(242, 162, 30, 1);
    --art-amber: rgba(233, 138, 18, 0.85);
    --art-orange-clear: rgba(242, 162, 30, 0);
    --art-red: rgba(168, 29, 16, 1);
    --art-red-soft: rgba(168, 29, 16, 0.85);
    --art-red-clear: rgba(168, 29, 16, 0);
    --art-green-light: rgba(159, 208, 106, 1);
    --art-green-dark: rgba(47, 90, 50, 0.9);
    --art-green-clear: rgba(47, 90, 50, 0);
    --art-earth: rgba(185, 169, 142, 0.75);
    --art-earth-soft: rgba(214, 202, 178, 0.35);
    --art-earth-clear: rgba(214, 202, 178, 0);
  }
  * { margin: 0; padding: 0; box-sizing: border-box; }
  html, body {
    width: 1200px;
    height: 830px;
    overflow: hidden;
    background: var(--page);
  }
  .label-sheet {
    position: relative;
    width: 1200px;
    height: 830px;
  }
  .wine-label {
    position: absolute;
    top: 58px;
    width: 568px;
    height: 710px;
    background: var(--label-paper);
    overflow: hidden;
  }
  .wine-label--red { left: 22px; }
  .wine-label--white { left: 606px; }

  .brand-name {
    position: absolute;
    top: 36px;
    left: 0;
    width: 100%;
    text-align: center;
    font-family: "Pinyon Script", cursive;
    font-weight: 400;
    font-size: 66px;
    line-height: 1;
    color: var(--ink);
  }
  .range-name {
    position: absolute;
    top: 116px;
    left: 0;
    width: 100%;
    text-align: center;
    font-family: "Josefin Sans", sans-serif;
    font-weight: 300;
    font-size: 23px;
    letter-spacing: 0.24em;
    padding-left: 0.24em;
    color: var(--accent-red);
  }

  .artwork {
    position: absolute;
    display: block;
  }
  .artwork--red {
    left: 118px;
    top: 144px;
    width: 360px;
    height: 430px;
    background:
      radial-gradient(ellipse 26% 20% at 50% 52%, var(--art-red) 0%, var(--art-red-soft) 55%, var(--art-red-clear) 100%),
      radial-gradient(ellipse 46% 45% at 52% 50%, var(--art-orange) 0%, var(--art-amber) 60%, var(--art-orange-clear) 100%);
  }
  .artwork--white {
    left: 140px;
    top: 150px;
    width: 320px;
    height: 430px;
    background:
      radial-gradient(ellipse 34% 24% at 48% 44%, var(--art-green-light) 0%, var(--art-green-dark) 60%, var(--art-green-clear) 100%),
      radial-gradient(ellipse 46% 46% at 50% 52%, var(--art-earth) 0%, var(--art-earth-soft) 60%, var(--art-earth-clear) 100%);
  }

  .seal {
    position: absolute;
    left: 402px;
    top: 482px;
    width: 110px;
    height: 110px;
  }

  .varietal {
    position: absolute;
    top: 556px;
    left: 0;
    width: 100%;
    text-align: center;
    font-family: "Cinzel", serif;
    font-weight: 600;
    font-size: 38px;
    line-height: 1;
    color: var(--ink);
  }
  .producer-line {
    position: absolute;
    top: 609px;
    left: 0;
    width: 100%;
    text-align: center;
    font-family: "Josefin Sans", sans-serif;
    font-weight: 300;
    font-size: 13.5px;
    letter-spacing: 0.1em;
    padding-left: 0.1em;
    color: var(--gold);
  }
  .origin {
    position: absolute;
    top: 634px;
    left: 0;
    width: 100%;
    text-align: center;
    font-family: "Josefin Sans", sans-serif;
    font-weight: 300;
    font-size: 22px;
    letter-spacing: 0.16em;
    padding-left: 0.16em;
    color: var(--gold);
  }
</style>
</head>
<body>
<main class="label-sheet">

  <section class="wine-label wine-label--red" aria-label="Red wine label">
    <h1 class="brand-name">Valora di Castegno</h1>
    <p class="range-name">BARREL SELECT</p>
    <div class="artwork artwork--red" role="img" aria-label="Painted red butterfly on broad orange brush strokes"></div>
    <svg class="seal" viewBox="0 0 110 110" role="img" aria-label="Vintage seal">
      <circle cx="55" cy="55" r="52" fill="none" stroke="var(--seal-line)" stroke-width="1.5"/>
      <circle cx="55" cy="55" r="46" fill="none" stroke="var(--seal-line)" stroke-width="1"/>
    </svg>
    <h2 class="varietal">Rosso</h2>
    <p class="producer-line">ARTISANLLY CRAFTED BY CANTINA VAL SERENA</p>
    <p class="origin">PIEMONTE ITALY</p>
  </section>

  <section class="wine-label wine-label--white" aria-label="White wine label">
    <h1 class="brand-name">Valora di Castegno</h1>
    <p class="range-name">BARREL SELECT</p>
    <div class="artwork artwork--white" role="img" aria-label="Painted green butterfly over soft earth-toned brush strokes"></div>
    <svg class="seal" viewBox="0 0 110 110" role="img" aria-label="Vintage seal">
      <circle cx="55" cy="55" r="52" fill="none" stroke="var(--seal-line)" stroke-width="1.5"/>
      <circle cx="55" cy="55" r="46" fill="none" stroke="var(--seal-line)" stroke-width="1"/>
    </svg>
    <h2 class="varietal">Rosso</h2>
    <p class="producer-line">ARTISANLLY CRAFTED BY CANTINA VAL SERENA</p>
    <p class="origin">PIEMONTE ITALY</p>
  </section>

</main>
</body>
</html>
```